Bramblewick Gardening Services. A6 flyer single sided

Need an A6 flyer designing. Single sided.
I am a gardener.
I do lawn mowing - one-off garden tidy ups or regular fortnightly visits.
All kinds of trees expertly felled, topped or pruned.
Hedge cutting.
Fencing replaced or repaired.
Fully insured.
Access to fully qualified and licenced tree arborist
07724 316048 or 01632 742918.

I have attached my business card and letter head logo.
I'm open to new designs without incorporating any of my artwork.

Industry/Entity Type

Gardener

```html
<!DOCTYPE html>
<html lang="en">
<head>
<meta charset="utf-8">
<title>Bramblewick Gardening Services – Flyer</title>
<link rel="stylesheet" href="https://fonts.googleapis.com/css2?family=Gelasio:ital,wght@0,400;0,700;1,400;1,700&display=swap">
<style>
  :root {
    --lime: #8cc63f;
    --slate: #5a6371;
    --text-grey: #5f6266;
    --hedge-dark: #2f5a22;
    --hedge-mid: #4d8a33;
    --hedge-light: #7fb94c;
    --lawn-light: #8ccc4a;
    --lawn-dark: #5fa52c;
    --panel: rgba(62, 104, 52, 0.92);
    --white: #ffffff;
  }
  * { margin: 0; padding: 0; box-sizing: border-box; }
  html, body { width: 851px; height: 1200px; overflow: hidden; background: var(--white); }
  .flyer {
    position: relative;
    width: 851px;
    height: 1200px;
    overflow: hidden;
    background: var(--white);
    font-family: "Gelasio", Georgia, serif;
  }
  .top-band {
    position: absolute; left: 0; top: 0;
    width: 100%; height: 21px;
    background: var(--lime);
  }
  .header {
    position: absolute; left: 0; top: 21px;
    width: 100%; height: 188px;
    background: var(--white);
    box-shadow: 0 3px 4px rgba(0, 0, 0, 0.22);
    display: flex; align-items: center; justify-content: center;
  }
  .business-name {
    font-weight: 700;
    font-size: 41px;
    color: var(--slate);
    letter-spacing: 0.2px;
    margin-top: -2px;
  }
  .services {
    position: absolute; left: 81px; top: 300px;
    list-style: none;
    color: var(--text-grey);
    font-style: italic;
    font-size: 33.5px;
    line-height: 41px;
    white-space: nowrap;
  }
  .services .note { font-size: 22px; }
  .services .insured { font-size: 28px; line-height: 46px; }
  .services .insured .note { font-size: 22px; }
  .garden-scene {
    position: absolute; left: 0; top: 625px;
    width: 100%; height: 575px;
    background:
      linear-gradient(to bottom,
        var(--hedge-light) 0px,
        var(--hedge-mid) 40px,
        var(--hedge-dark) 200px,
        var(--hedge-mid) 360px,
        var(--hedge-dark) 462px,
        var(--lawn-light) 465px,
        var(--lawn-dark) 575px);
  }
  .contact-panel {
    position: absolute; left: 318px; top: 760px;
    width: 533px; height: 245px;
    background: var(--panel);
    border-radius: 122px 0 0 122px;
    box-shadow: 0 2px 6px rgba(0, 0, 0, 0.25);
  }
  .contact-panel .call, .contact-panel .phone {
    position: absolute; right: 76px;
    color: var(--white);
    font-weight: 700;
    text-shadow: 3px 3px 2px rgba(0, 0, 0, 0.75);
    white-space: nowrap;
  }
  .contact-panel .call { top: 26px; font-size: 54px; }
  .contact-panel .phone { font-style: italic; font-size: 47px; }
  .contact-panel .phone.mobile { top: 96px; }
  .contact-panel .phone.landline { top: 160px; }
  .email {
    position: absolute; left: 0; top: 1112px;
    width: 100%;
    text-align: center;
    color: var(--white);
    font-size: 28px;
    letter-spacing: 6.2px;
  }
</style>
</head>
<body>
  <main class="flyer">
    <div class="top-band"></div>
    <header class="header">
      <h1 class="business-name">Bramblewick Gardening Services</h1>
    </header>

    <ul class="services">
      <li>Lawn Mowing - <span class="note">Fortnightly Visits or 1 Off Garden Tidy-Ups</span></li>
      <li>Hedge Cutting</li>
      <li>Fencing - Replaced &amp; Repaired</li>
      <li>Trees felled, topped and pruned</li>
      <li>Access to a licensed tree arborist</li>
      <li class="insured">FULLY INSURED <span class="note">(£5,000,000 public liability insurance)</span></li>
    </ul>

    <div class="garden-scene" role="img" aria-label="Photograph of a neatly trimmed green hedge above a mown lawn"></div>

    <section class="contact-panel">
      <p class="call">Ring Owen</p>
      <p class="phone mobile">07724 316048</p>
      <p class="phone landline">01632 742918</p>
    </section>

    <p class="email">bramblewick@example.com</p>
  </main>
</body>
</html>
```